Buch-/eBook-Cover für ein jährlichen Referenzbuchs der Industrie
Zielgruppe
verlag-technova ist ein Fachverlag mit Fokus auf Industrie und Technologie. Seit über 30 Jahren entwickeln wir Medienangebote für Technologiemärkte – immer mit dem Ziel, komplexe Inhalte verständlich und ansprechend aufzubereiten.
Unsere Arbeit basiert auf einer echten Begeisterung für Technik. Mit unseren Marken bauen wir Brücken zwischen Anbietern und Anwendern – in Print, digital und auf Events.
Wir veröffentlichen Magazine, organisieren Veranstaltungen und entwickeln für Kunden individuelle Kommunikationskampagnen. Unsere Plattformen sind in ihren Zielbranchen fest etabliert und genießen ein hohes Maß an Vertrauen.
Bei dem ausgeschriebenen Projekt handelt es sich um unser FABRIK.vorlauf MOLUVENA – Das Referenzbuch der Industrie, welches jährlich erscheint. MOLUVENA ist aus dem polynesischen Sprachraum und steht für Freiraum.
FABRIK.vorlauf MOLUVENA ist ein Referenzbuch, das den Namen verdient: unkonventionell, hochrelevant, emotional, motivierend. Bewusst umgesetzt als hochwertige Print-Referenzpublikation!
Wandel bestimmt unsere Zeit und verändert unsere Gesellschaft, unsere Unternehmen, uns alle.
Im Wandel liegt Freiraum zur Gestaltung. Gesellschaftlicher Wandel, Technologie-Wandel, Klimawandel, Wertewandel, Führungswandel oder Organisationswandel sind nur einige Beispiele. Wer dabei den Wandel in engen Bahnen denkt, verschenkt Potential. Veränderung braucht Freiraum für neue Ideen und Perspektiven sowie Persönlichkeiten, die diesen nutzen wollen.
Unsere Leserzielgruppe – Vorwärtsdenker und Zukunftsmacher:
Strategische & technische Entscheider in der Industrie: Inhaber, Vorstand, Geschäftsführer, Betriebs- & Werksleiter, Bereichs-, Gruppen-, Abteilungs- und Projektleiter
Redaktionelles Konzept:
Wer gestaltet die Zukunft der Industrie und ihrer Branchen? Und wie?
Wir geben Personen aus der Industrie den Freiraum, ihre P..
Aufgabenstellung
1.) Kurzzusammenfassung der Ausschreibung
Die 6. Ausgabe des jährlichen Referenzbuchs der Industrie, FABRIK.vorlauf MOLUVENA 2026, erscheint im Oktober 2025. Für das Cover sucht verlag-technova neue Vorschläge, die nicht automatisch eine Fortsetzung der vorherigen Titel sind.
2.) Gestalterische & Inhaltliche Anforderungen
• Format: 195x250 mm + 3 mm Anschnitt
• Rücken: ca. 1,3 cm (Stand letzte Publikation 2024)
• Auflösung: Druckqualität, mind. 300 dpi
• Inhaltliche Elemente:
- Cover
MOLUVENA 2026 Schriftzug (Orientierung egal)
{polynesisch: Freiraum}
Untersatz: Das Referenzbuch der Industrie. Für Vorwärtsdenker und Zukunftsmacher.
part of FABRIK.vorlauf Logo-Balken am unteren Rand (siehe Beispiel-Cover MOLUVENA 2025)
3 Statements (je 100-150 Zeichen mit Leerzeichen), zu verwendende Schrift: Helvetica Neue LT Std
Folgende Statements dienen als Beispiel und müssen im Nachgang noch angepasst werden
ERFOLG DURCH FLEXIBILITÄT: IT-ARCHITEKTUREN UND KI TRANSFORMIEREN UNTERNEHMEN GRUNDLEGEND!
PRODUKTIONSFOOTPRINT DEUTSCHER MITTELSTAND 2030+: REGIONAL, 100 % AUTOMATISIERT, KLIMANEUTRAL!
UNTERNEHMEN, DIE FLEXIBEL UND ADAPTIV SIND, KÖNNEN CHANCEN NUTZEN UND INNOVATIONSFÜHRER BLEIBEN.
- Rücken:
MOLUVENA
Jahreszahl: 2026
Zu verwendende Schrift: Helvetica Neue LT Std
WICHTIG: Die Farbe Orange (0/80/100/0) soll als Wiedererkennung in die Gestaltungen eingebunden werden. Wir geben die Cover der vergangenen Jahre als Beispiel und Orientierung mit, möchten aber abgesehen von der Farbe bewusst in eine neue Richtung gehen. Bei der Orientierung und Platzierung der Schriftzüge gibt es daher keine Vorgaben. Zu den Beispiel-Cover MOLUVENA: https://www.fachwelt-verlag.de/de/MoluVena/e-paper
Das Design darf nicht zu überladen sein.

```html
<!DOCTYPE html>
<html lang="de">
<head>
<meta charset="utf-8">
<title>MOLUVENA 2026 – Cover</title>
<link rel="stylesheet" href="https://fonts.googleapis.com/css2?family=Inter:wght@400;500;600&display=swap">
<style>
  :root {
    --stage: #141414;
    --ink: #0d0d0d;
    --orange: #f26a2e;
    --orange-deep: #e0541e;
    --white: #f2f2f2;
    --grey: #8a8a8a;
    --grey-dark: #3a3a3a;
  }
  * { margin: 0; padding: 0; box-sizing: border-box; }
  html, body { width: 1200px; height: 900px; overflow: hidden; background: var(--stage); }
  body { font-family: "Inter", "Helvetica Neue", Arial, sans-serif; position: relative; }

  .cover {
    position: absolute;
    top: 114px;
    width: 488px;
    height: 664px;
    overflow: hidden;
  }
  .cover--dark { left: 87px; background: var(--ink); color: var(--white); }
  .cover--orange { left: 627px; background: var(--orange); color: var(--ink); }

  .cover__title {
    position: absolute;
    left: 34px;
    top: 30px;
    font-weight: 600;
    font-size: 74px;
    line-height: 84px;
    letter-spacing: -2px;
  }
  .cover__tag {
    position: absolute;
    left: 390px;
    top: 128px;
    width: 58px;
    height: 13px;
    font-size: 7px;
    font-weight: 600;
    letter-spacing: 0.5px;
    line-height: 13px;
    text-align: center;
  }
  .cover--dark .cover__tag { background: var(--orange); color: var(--ink); }
  .cover--orange .cover__tag { background: var(--ink); color: var(--orange); }

  .cover__subtitle {
    position: absolute;
    left: 34px;
    top: 200px;
    font-size: 17px;
    font-weight: 400;
  }

  .cover__art {
    position: absolute;
    left: 0;
    top: 240px;
    width: 488px;
    height: 280px;
  }
  .cover--dark .cover__art {
    background: linear-gradient(90deg, #6e6e6e 0%, #2a2a2a 35%, #b0b0b0 50%, #f26a2e 62%, #1a1a1a 75%, #e0541e 100%);
  }
  .cover--orange .cover__art {
    background: linear-gradient(90deg, #9a9a9a 0%, #1c1c1c 30%, #2a2a2a 50%, #1c1c1c 68%, #6e6e6e 82%, #1a1a1a 100%);
  }

  .cover__imprint-bar {
    position: absolute;
    left: 34px;
    top: 617px;
    font-size: 14px;
    font-weight: 400;
  }
  .cover__imprint {
    position: absolute;
    right: 28px;
    top: 592px;
    display: flex;
    align-items: center;
    gap: 6px;
    font-size: 11px;
    font-weight: 500;
  }
  .cover__imprint-dot { width: 30px; height: 30px; border-radius: 50%; }
  .cover--dark .cover__imprint-dot { background: var(--white); }
  .cover--orange .cover__imprint-dot { background: var(--ink); }
</style>
</head>
<body>

<section class="cover cover--dark">
  <h1 class="cover__title">MOLUVENA<br>2026</h1>
  <div class="cover__tag">FREIRAUM</div>
  <p class="cover__subtitle">Polynesian: Freiraum</p>
  <div class="cover__art" role="img" aria-label="Abstrakte Illustration aus Halbkugeln, Kugeln und Wellen in Grau, Weiß und Orange"></div>
  <p class="cover__imprint-bar">part of FABRIK.vorlauf</p>
  <div class="cover__imprint"><span>technova</span><span class="cover__imprint-dot"></span></div>
</section>

<section class="cover cover--orange">
  <h1 class="cover__title">MOLUVENA<br>2026</h1>
  <div class="cover__tag">FREIRAUM</div>
  <p class="cover__subtitle">Polynesisch</p>
  <div class="cover__art" role="img" aria-label="Abstrakte Illustration aus Halbkugeln, gemusterten Kugeln und Wellen in Schwarz und Grau"></div>
  <p class="cover__imprint-bar">part of FABRIK.vorlauf</p>
  <div class="cover__imprint"><span>technova</span><span class="cover__imprint-dot"></span></div>
</section>

</body>
</html>
```